Business card design needed

I need a simple business card design with contact details on one side (and a logo) and 2 logos on the other side. I would like the text to be in silver and the card black.

Target Market(s)

Luxury market

Industry/Entity Type

Business

Contact Information for Business Card

M&K Forvela, PO BOX 517, Brindlecoe, VIC, 3186

Logo Text

M&K Forvela

Requirements
Must have
• black card, 2 logos on back, M&K logo on front

Text on front should be

Neil & Priya Haverstock

Neil 0417826391 Priya 0428650147
neil@mkforvela.com priya@mkforvela.com
PO BOX 517, Brindlecoe, VIC, 3186

```html
<!DOCTYPE html>
<html lang="en">
<head>
<meta charset="utf-8">
<title>M&amp;K Forvela Business Card</title>
<link href="https://fonts.googleapis.com/css2?family=Josefin+Sans:wght@300;400&family=Open+Sans:wght@400&family=Playfair+Display:wght@400&display=swap" rel="stylesheet">
<style>
  :root {
    --backdrop: #1b1b1b;
    --card: #050505;
    --card-edge: #3a3a3a;
    --silver: #e2e2e2;
    --silver-soft: #c9c9c9;
  }
  * { margin: 0; padding: 0; box-sizing: border-box; }
  html, body {
    width: 1200px;
    height: 1000px;
    overflow: hidden;
    background: var(--backdrop);
  }
  .stage {
    position: relative;
    width: 1200px;
    height: 1000px;
  }
  .card {
    position: absolute;
    left: 250px;
    width: 700px;
    height: 400px;
    background: var(--card);
    border: 1px solid var(--card-edge);
    color: var(--silver);
  }
  .card--back { top: 60px; }
  .card--front { top: 540px; }

  /* Back side: two brand names */
  .partner-mark {
    position: absolute;
    left: 90px;
    top: 150px;
    width: 260px;
    text-align: center;
  }
  .partner-mark__square {
    display: block;
    width: 46px;
    height: 46px;
    margin: 0 auto 26px;
    background: var(--silver);
    border-radius: 4px;
  }
  .partner-mark__name {
    font-family: "Josefin Sans", sans-serif;
    font-weight: 400;
    font-size: 17px;
    letter-spacing: 7px;
    text-transform: uppercase;
  }
  .brand-mark--back {
    position: absolute;
    left: 400px;
    top: 170px;
    width: 220px;
    text-align: center;
    font-family: "Playfair Display", serif;
    font-size: 28px;
    line-height: 1.25;
  }

  /* Front side: brand and contacts */
  .brand-mark--front {
    position: absolute;
    left: 60px;
    top: 110px;
    width: 300px;
    text-align: center;
    font-family: "Playfair Display", serif;
    color: var(--silver);
  }
  .brand-mark__initials {
    display: block;
    font-size: 64px;
    line-height: 1.1;
  }
  .brand-mark__word {
    display: block;
    font-size: 30px;
    margin-top: 12px;
  }
  .postal-address {
    position: absolute;
    left: 70px;
    top: 310px;
    font-family: "Open Sans", sans-serif;
    font-size: 14px;
    letter-spacing: 0.6px;
    font-style: normal;
  }
  .contacts {
    position: absolute;
    left: 390px;
    top: 50px;
    width: 290px;
  }
  .contacts__couple {
    font-family: "Josefin Sans", sans-serif;
    font-weight: 300;
    font-size: 18px;
    line-height: 1.3;
    text-transform: uppercase;
    margin-bottom: 32px;
  }
  .person { margin-left: 10px; margin-bottom: 22px; }
  .person + .person { margin-left: 20px; }
  .person__name {
    font-family: "Josefin Sans", sans-serif;
    font-weight: 400;
    font-size: 15px;
    letter-spacing: 1px;
    text-transform: uppercase;
    margin-bottom: 4px;
  }
  .person__line {
    font-family: "Open Sans", sans-serif;
    font-size: 13px;
    line-height: 1.45;
    letter-spacing: 0.6px;
    color: var(--silver-soft);
    padding-left: 4px;
  }
</style>
</head>
<body>
<main class="stage">
  <section class="card card--back" aria-label="Card back">
    <div class="partner-mark">
      <span class="partner-mark__square"></span>
      <span class="partner-mark__name">Brunnhalde</span>
    </div>
    <div class="brand-mark--back">M&amp;K<br>Forvela</div>
  </section>

  <section class="card card--front" aria-label="Card front">
    <div class="brand-mark--front">
      <span class="brand-mark__initials">M&amp;K</span>
      <span class="brand-mark__word">Forvela</span>
    </div>
    <address class="postal-address">PO BOX 517, Brindlecoe, VIC, 3186</address>

    <div class="contacts">
      <p class="contacts__couple">Neil &amp; Priya<br>Haverstock</p>
      <div class="person">
        <p class="person__name">Neil Haverstock</p>
        <p class="person__line">PhoneNo.: 0417826391</p>
        <p class="person__line">neil@mkforvela.com</p>
      </div>
      <div class="person">
        <p class="person__name">Priya Haverstock</p>
        <p class="person__line">PhoneNo.: 0428650147</p>
        <p class="person__line">priya@mkforvela.com</p>
      </div>
    </div>
  </section>
</main>
</body>
</html>
```